Osmer wine Label, 750ml bottle

We need a wine label that is simple, clean, and timeless. The final project should reflect a premium product. All ideas encouraged. A label that is eye catching and gives of a pristine look. The wine is a Red Blend of Zinfandel, Syrah, Grenache, and Tempranillo. All Californian fruit and hand crafted. The wine is really something special and the label should reflect that. The label must also be able to carry many tiers, the addition of some other labels based around this label may take place in the future.

Target Market(s)

All ideas welcome

Industry/Entity Type

Retail

Font styles to use
Serif

Requirements
Must have
• Open to all ideas.
Nice to have
• An elegant look, simple colors, however, some sort of eye catching effect.
Should not have
• Should not be quirky.

```html
<!DOCTYPE html>
<html lang="en">
<head>
<meta charset="utf-8">
<title>Osmer – Red Blend Wine Label</title>
<link rel="stylesheet" href="https://fonts.googleapis.com/css2?family=Playfair+Display:wght@700;900&family=Montserrat:wght@500&display=swap">
<style>
  :root {
    --backdrop: #e8e5de;
    --label-deep: #3a1b44;
    --label-purple: #6b3a80;
    --label-violet: #8c55a3;
    --label-dark: #24122b;
    --copper: #e6a57c;
    --ivory: #ffffff;
    --tab-purple: #7a4690;
  }
  * { margin: 0; padding: 0; box-sizing: border-box; }
  html, body {
    width: 1200px;
    height: 924px;
    overflow: hidden;
    background: var(--backdrop);
  }
  .canvas {
    position: relative;
    width: 1200px;
    height: 924px;
  }
  .label {
    position: absolute;
    left: 350px;
    top: 140px;
    width: 500px;
    height: 740px;
    overflow: hidden;
    box-shadow: 0 6px 24px rgba(40, 20, 50, 0.18);
  }
  .label-texture {
    position: absolute;
    inset: 0;
    width: 100%;
    height: 100%;
  }
  .brand-tab {
    position: absolute;
    left: 515px;
    top: 72px;
    width: 170px;
    height: 170px;
    background: var(--tab-purple);
    border: 9px solid var(--ivory);
    display: flex;
    align-items: center;
    justify-content: center;
    z-index: 2;
  }
  .brand-tab-name {
    font-family: "Playfair Display", serif;
    font-weight: 700;
    font-size: 36px;
    color: var(--ivory);
    letter-spacing: 1px;
  }
  .wine-name {
    position: absolute;
    left: 0;
    right: 0;
    top: 290px;
    text-align: center;
    font-family: "Playfair Display", serif;
    font-weight: 900;
    font-size: 92px;
    letter-spacing: 6px;
    line-height: 1;
    color: var(--copper);
  }
  .grape-list {
    position: absolute;
    left: 140px;
    top: 488px;
    list-style: none;
    font-family: "Montserrat", sans-serif;
    font-weight: 500;
    font-size: 14px;
    line-height: 20px;
    letter-spacing: 0.5px;
    color: var(--ivory);
  }
  .region {
    position: absolute;
    left: 0;
    right: 0;
    top: 612px;
    text-align: center;
    font-family: "Playfair Display", serif;
    font-weight: 700;
    font-size: 28px;
    letter-spacing: 2px;
    color: var(--ivory);
  }
  .label-footer {
    position: absolute;
    left: 30px;
    right: 30px;
    bottom: 22px;
    display: flex;
    justify-content: space-between;
    align-items: baseline;
    color: var(--ivory);
  }
  .volume, .abv {
    font-family: "Montserrat", sans-serif;
    font-weight: 500;
    font-size: 18px;
    letter-spacing: 0.5px;
  }
  .vintage {
    font-family: "Playfair Display", serif;
    font-weight: 700;
    font-size: 30px;
    letter-spacing: 1px;
  }
</style>
</head>
<body>
<main class="canvas">
  <section class="label">
    <svg class="label-texture" viewBox="0 0 500 740" preserveAspectRatio="none" role="img" aria-label="Purple marbled ink texture across the label">
      <defs>
        <linearGradient id="marble-base" x1="0" y1="0" x2="1" y2="1">
          <stop offset="0" stop-color="#4a2458"/>
          <stop offset="0.3" stop-color="#7b4692"/>
          <stop offset="0.55" stop-color="#5a2d6c"/>
          <stop offset="0.8" stop-color="#7a4690"/>
          <stop offset="1" stop-color="#2e1636"/>
        </linearGradient>
        <radialGradient id="marble-glow" cx="0.55" cy="0.35" r="0.6">
          <stop offset="0" stop-color="#9a62b2" stop-opacity="0.55"/>
          <stop offset="1" stop-color="#9a62b2" stop-opacity="0"/>
        </radialGradient>
      </defs>
      <rect width="500" height="740" fill="url(#marble-base)"/>
      <rect width="500" height="740" fill="url(#marble-glow)"/>
    </svg>
    <h1 class="wine-name">OSMER</h1>
    <ul class="grape-list">
      <li>ZINFANDEL</li>
      <li>SYRAH</li>
      <li>GRENACHE</li>
      <li>TEMPRANILLO</li>
    </ul>
    <p class="region">CALIFORNIA</p>
    <footer class="label-footer">
      <span class="volume">75cl</span>
      <span class="vintage">2016</span>
      <span class="abv">15% vol.</span>
    </footer>
  </section>
  <div class="brand-tab">
    <span class="brand-tab-name">Osmer</span>
  </div>
</main>
</body>
</html>
```